Vantrel Ashcombe LLC

we need a business card design

Industry/Entity Type

hvac

Contact Information for Business Card

my logo

Requirements
Must have
• my logo and same colors

```html
<!DOCTYPE html>
<html lang="en">
<head>
<meta charset="utf-8">
<title>Vantrel Ashcombe LLC – Business Card</title>
<link rel="stylesheet" href="https://fonts.googleapis.com/css2?family=Montserrat:wght@400;500;700&display=swap">
<style>
  :root {
    --page-bg: #e4e5e7;
    --card-bg: #ffffff;
    --brand-blue: #1a5aa8;
    --brand-yellow: #f6b94a;
    --ink: #1d1d1f;
    --rule: #3f5a7a;
  }
  * { box-sizing: border-box; margin: 0; padding: 0; }
  html, body {
    width: 1200px; height: 875px; overflow: hidden;
    background: var(--page-bg);
    font-family: "Montserrat", sans-serif;
    color: var(--ink);
  }
  .sheet {
    width: 1200px; height: 875px;
    display: flex; flex-direction: column; align-items: center; justify-content: center;
    gap: 36px;
  }
  .card {
    position: relative;
    width: 630px; height: 360px;
    background: var(--card-bg);
    border-radius: 22px;
    overflow: hidden;
    box-shadow: 0 6px 18px rgba(0,0,0,0.12);
  }
  .brand-mark {
    display: flex; align-items: center; gap: 12px;
    color: var(--brand-blue);
    font-weight: 700;
  }
  .brand-mark .dot {
    width: 22px; height: 22px; border-radius: 50%;
    background: var(--brand-blue); flex: none;
  }
  .card-front { display: flex; align-items: center; justify-content: center; }
  .card-front .brand-mark { font-size: 34px; }

  .card-back .brand-mark {
    position: absolute; left: 48px; top: 128px;
    font-size: 22px; width: 230px; line-height: 1.2;
  }
  .divider {
    position: absolute; left: 300px; top: 70px;
    width: 1.5px; height: 160px; background: var(--rule);
  }
  .contact {
    position: absolute; left: 328px; top: 64px;
  }
  .contact .person-name {
    color: var(--brand-blue); font-weight: 700; font-size: 27px; letter-spacing: 0.2px;
  }
  .contact .person-role { font-size: 17px; margin: 2px 0 14px; }
  .contact ul { list-style: none; }
  .contact li {
    display: flex; align-items: center; gap: 12px;
    font-size: 14.5px; line-height: 24px;
  }
  .contact svg { width: 15px; height: 15px; fill: var(--brand-blue); flex: none; }
  .address {
    position: absolute; left: 0; right: 0; top: 262px;
    text-align: center; font-size: 14.5px;
  }
  .footer-band { position: absolute; left: 0; bottom: 0; width: 100%; height: 26px; }
</style>
</head>
<body>
<main class="sheet">
  <section class="card card-front">
    <div class="brand-mark"><span class="dot"></span><span>Vantrel Ashcombe LLC</span></div>
  </section>

  <section class="card card-back">
    <div class="brand-mark"><span class="dot"></span><span>Vantrel Ashcombe LLC</span></div>
    <div class="divider"></div>
    <div class="contact">
      <p class="person-name">Dorian Kessway</p>
      <p class="person-role">Owner</p>
      <ul>
        <li><svg viewBox="0 0 16 16"><path d="M2 5c0-1 1-2 6-2s6 1 6 2v1h-3V5H5v1H2zM4 7h8l2 6H2z"/></svg>044-123 456 789</li>
        <li><svg viewBox="0 0 16 16"><path d="M3 2l3 0 1 3-2 1.5c1 2 2.5 3.5 4.5 4.5L11 9l3 1v3c-6 1-12-5-11-11z"/></svg>044-123 456 789</li>
        <li><svg viewBox="0 0 16 16"><path d="M1 4h14v9H1zM1 4l7 5 7-5" stroke="#fff" stroke-width="1"/></svg>info@webname.com</li>
        <li><svg viewBox="0 0 16 16"><circle cx="8" cy="8" r="7"/><path d="M1 8h14M8 1v14M3 4h10M3 12h10" stroke="#fff" stroke-width="0.9" fill="none"/></svg>www.websitename.com</li>
      </ul>
    </div>
    <p class="address">421, Address line goes here 45452, Country name</p>
    <svg class="footer-band" viewBox="0 0 630 26" preserveAspectRatio="none">
      <polygon points="0,14 380,14 372,26 0,26" fill="var(--brand-blue)"/>
      <polygon points="392,0 630,0 630,26 380,26" fill="var(--brand-yellow)"/>
    </svg>
  </section>
</main>
</body>
</html>
```